Tolliver for Governor
We have chosen draft #108.
You have all done a great job and are amazing designers. I hope to work with you all again on future design projects for Tolliver For Governor.
Envelope: Move the address and URL up to just below the gold swoosh and you're missing a 't' in www.TolliverForGovernor.example On the back make the whole back white again add back in the emblem on the flap and make the It's Our Time fit across the back of the envelope in blue with a gradient.
Cards: Please see image and message.
Letterhead: Spot on!!!
We are now looking at #102, #103 and #106. Thank you to all the other designers, you've done a great job. There is still time for everyone to revise and resubmit their drafts, based on the comments we've made.
#90, Remove the email address from the letterhead and add Paid For By Tolliver For Governor on the same line as tolliverforgovernor.example, but on the far left side of page. Add address next to logo on front of envelope and lower It's Our Time on the back of the envelope. Remove the vertical It's Our Time from the two blue cards and center the logo on the blue card that should have no text.
#87, I like it. But everywhere you have tolliverforgovernor.example (except email addresses) remove it. I don't actually want the ""s around It's Our Time. It was away of telling you all what the exact text was. On the left side, the bottom two cards you could replace the URL with It's Our Time, just make the text bigger and bolder.
Envelope: I would like to see the back panel (not the flap) blue with white text saying "It's Our Time". On the front, move the address to the right side of the logo just under the gold swish. Add the URL under the address. Also, the address should be on 2 lines
P.O. Box 71832
Indianapolis, IN 46917
www.TolliverForGovernor.example
Card:
Logo-side, make the text much bigger (across the card bottom) and diffuse and spread out the white halo.
Info-side, move the phone number to it's own line above the address and move Name and title lines up to the lowest point in the gold swoosh. Try making the "tolliverforgovernor" in www.tolliverforgovernor.example blue like Jorel Drennick and capitalize the R,F and G.
Letterhead: on the same line as the phone and URL, but on the left side of the page, need "Paid For By Tolliver For Governor". Move the watermark logo up the page a little bit and add the line "It's Our Time" as light gray-ish watermark under it.
I done, please check
#80, please remove the URL from the logo-sides and insert the address on the info-side
please check private message
#45 and #43, let's lighten the background on the logo-side, remove the URL from both sides and insert the address.
#46, can we make the logo on the left side bigger, raise the name/title up more, insert the address and make the text bolder. On the logo side, lighter and more diffused. Also, please upload drafts for a letterhead and envelope.
I meant the logo-sides from #72 and #74
ALL: please include "Paid For By Tolliver For Governor" in small font at the bottom of the letterhead.
#70, this may be confusing, bare with me.
I like the info-side from #70 but; with the address added, name/title moved up and name in blue and remove the "phone" & "email" tags.
I like the logo-side but; make the white border around the logo the same size as the info-side and replace the URL with "It's Our Time" in font/style like "for Governor".
Would you be willing to add in the logo-side cards from both #71 and #74? Could you make the white border around the logos like the ones on the info-side in #70?
Also, need your drafts for an envelope and letterhead.
#13, I like the gradient on the front. Let's lighten the gradient, make the logo bigger and add some white diffusion around the logo (subtle). On the info side - like the flame in the lower corner. Raise the name and title area, make the name a little darker, remove the URL from the blue band, remove the "phone" and "email" tags, insert the full address. Maybe fill the center with a watermark of the logo? Also, would like to see some drafts for the letterhead and envelope.
Cards:
Info side- move name and title up more, put in the full address and add "It's Our Time" across the bottom in the same font style as "Tolliver".
Logo side- keep the logo transparency in the center of the logo, make the logo bigger and replace the white background with a light blue gradient (like in the images we uploaded).
Letterhead: remove all contact info except address, phone and URL. Add a "watermark" of all or part of the logo (w/ out the "Tolliver"). Also, at the bottom in the same line as the URL, but on the left side, add "Paid For By Tolliver For Governor".
Envelope: Insert the full address, move address and URL to the right of the logo (just under the gold line) on the back (not the flap) add "It's Our Time" feel free to try different colors in that area.
ALL: the card does not need to say "phone" or "email". You can use an icon if you want, but no need to spell it out. Also, only have the address, phone and URL on the letterhead.
Vandrel (#65,#64,#63,#62,#61,#60), What happened to the logo? Why is there sections (like a bar going across it) missing?
Sorry everyone, We've been on the road and unable to post more information or critiques.
Project Details:
1. This is a full stationary project (2-side business card, letterhead and envelope).
2. Front of business card should have either "It's Our Time" and the emblem from our provided logo or just the emblem. Background should be a light blue radial gradient with very light whitening behind emblem and/or text. Font for "It's Our Time" should match the fonts used for "Tolliver" in provided logo (colors either the same or white).
3. Address is:
PO Box 71832
4. Letterhead should have a watermark using all or part of the emblem from the provided logo.
5. Envelope should have a return address (PO Box from above).
6. Our campaign slogan is "It's Our Time".
7. On the business card there needs to be an area between the name/title area and the contact info.
8. Please do not fill in the transparent parts of the emblem or change it's color.
We will be picking a winner in the next 24 hours or less.
Good luck everyone :)

```html
<!DOCTYPE html>
<html lang="en">
<head>
<meta charset="utf-8">
<title>Tolliver for Governor — Stationery Set</title>
<link rel="stylesheet" href="https://fonts.googleapis.com/css2?family=Libre+Baskerville:wght@700&family=Arimo:wght@400;700&display=swap">
<style>
  :root{
    --stage:#ffffff;
    --frame:#e4e6ea;
    --paper:#ffffff;
    --edge:#d5d8dd;
    --blue:#1b5aa8;
    --blue-deep:#0f3f82;
    --gold:#a6874f;
    --ink-soft:#8a7550;
    --flap-line:#9a9ea6;
  }
  *{margin:0;padding:0;box-sizing:border-box}
  html,body{width:1200px;height:681px;overflow:hidden;background:var(--stage)}
  .board{position:relative;width:1200px;height:681px;background:var(--stage)}
  .board-frame{position:absolute;left:19px;top:41px;width:1162px;height:607px;border:1px solid var(--frame)}
  .sheet{position:absolute;background:var(--paper);border:1px solid var(--edge);overflow:hidden}
  .swoosh{position:absolute;left:0;top:0;width:100%;display:block}
  .emblem-disc{position:absolute;border-radius:50%;background:var(--blue);border:3px solid var(--paper);box-shadow:0 0 0 1px var(--edge)}
  .wordmark{position:absolute;font-family:"Libre Baskerville",Georgia,serif;font-weight:700;color:var(--blue);letter-spacing:.5px;white-space:nowrap}
  .fine{position:absolute;font-family:Arimo,Arial,sans-serif;color:var(--ink-soft);white-space:nowrap}

  /* envelope front */
  .envelope-front{left:62px;top:101px;width:334px;height:211px}
  .envelope-front .swoosh{height:64px}
  .envelope-front .emblem-disc{left:22px;top:14px;width:60px;height:60px}
  .envelope-front .wordmark{left:14px;top:80px;font-size:27px}
  .envelope-front .fine{left:16px;top:122px;font-size:6.5px}

  /* envelope back */
  .envelope-back{left:62px;top:360px;width:334px;height:216px}
  .envelope-back .flap{position:absolute;left:0;top:0;width:100%;height:100px}
  .envelope-back .emblem-disc{left:144px;top:22px;width:48px;height:48px}

  /* letterhead */
  .letterhead{left:619px;top:48px;width:377px;height:576px}
  .letterhead .swoosh{height:96px}
  .letterhead .emblem-disc{left:42px;top:44px;width:60px;height:60px}
  .letterhead .wordmark{left:20px;top:104px;font-size:33px}
  .letterhead .footer-line{right:18px;font-size:6px;text-align:right}
  .letterhead .footer-line.contact{top:530px}
  .letterhead .footer-line.web{top:542px}

  /* business card, info side */
  .card-info{left:967px;top:180px;width:197px;height:108px}
  .card-info .swoosh{height:40px}
  .card-info .emblem-disc{left:14px;top:8px;width:28px;height:28px;border-width:2px}
  .card-info .wordmark{left:7px;top:38px;font-size:13px}
  .card-info .name{position:absolute;right:12px;top:43px;font-family:Arimo,Arial,sans-serif;font-weight:700;font-size:7.5px;color:var(--blue)}
  .card-info .title{right:12px;top:53px;font-size:5.5px}
  .card-info .contact{right:10px;font-size:5px;text-align:right}
  .card-info .contact.phone{top:76px}
  .card-info .contact.address{top:84px}
  .card-info .contact.web{top:92px}

  /* business card, emblem side */
  .card-emblem{left:967px;top:312px;width:197px;height:108px}
  .card-emblem .emblem-disc{left:72px;top:28px;width:52px;height:52px}
</style>
</head>
<body>
<main class="board">
  <div class="board-frame"></div>

  <section class="sheet envelope-front" aria-label="Envelope front">
    <svg class="swoosh" viewBox="0 0 334 64" preserveAspectRatio="none" aria-hidden="true">
      <path d="M0 0H334V10C250 0 170 34 0 30Z" fill="var(--blue)"/>
      <path d="M0 30C170 34 250 0 334 10V16C250 8 170 44 0 42Z" fill="var(--gold)"/>
    </svg>
    <div class="emblem-disc"></div>
    <div class="wordmark">Tolliver</div>
    <p class="fine">P.O. Box 71832 · Indianapolis, IN 46917 · www.TolliverForGovernor.example</p>
  </section>

  <section class="sheet envelope-back" aria-label="Envelope back">
    <svg class="flap" viewBox="0 0 334 100" preserveAspectRatio="none" aria-hidden="true">
      <path d="M0 0L20 60Q167 100 314 60L334 0" fill="none" stroke="var(--flap-line)" stroke-width="1"/>
    </svg>
    <div class="emblem-disc"></div>
  </section>

  <section class="sheet letterhead" aria-label="Letterhead">
    <svg class="swoosh" viewBox="0 0 377 96" preserveAspectRatio="none" aria-hidden="true">
      <path d="M0 0H377V14C280 0 170 52 0 50Z" fill="var(--blue)"/>
      <path d="M0 50C170 52 280 0 377 14V22C280 10 170 66 0 64Z" fill="var(--gold)"/>
    </svg>
    <div class="emblem-disc"></div>
    <div class="wordmark">Tolliver</div>
    <p class="fine footer-line contact">P.O. Box 71832 | Indianapolis, IN 46917 | (317) 555-0142</p>
    <p class="fine footer-line web">www.TolliverForGovernor.example | Paid For By Tolliver For Governor</p>
  </section>

  <section class="sheet card-info" aria-label="Business card, information side">
    <svg class="swoosh" viewBox="0 0 197 40" preserveAspectRatio="none" aria-hidden="true">
      <path d="M0 0H197V6C140 0 90 22 0 20Z" fill="var(--blue)"/>
      <path d="M0 20C90 22 140 0 197 6V10C140 6 90 30 0 28Z" fill="var(--gold)"/>
    </svg>
    <div class="emblem-disc"></div>
    <div class="wordmark">Tolliver</div>
    <p class="name">Jorel Drennick</p>
    <p class="fine title">Candidate for Governor</p>
    <p class="fine contact phone">(317) 555-0142</p>
    <p class="fine contact address">P.O. Box 71832 · Indianapolis, IN 46917</p>
    <p class="fine contact web">jdrennick@tolliverforgovernor.example</p>
  </section>

  <section class="sheet card-emblem" aria-label="Business card, emblem side">
    <div class="emblem-disc"></div>
  </section>
</main>
</body>
</html>
```